Cleaning Company Website Design

I am looking for a website design that has my contact information on each page (Call or Text and my e-mail). It should have the main landing page and than pages for Residential Cleaning (Move In/Move Out, Weekly, and Bi-Weekly Cleaning), Commercial Cleaning (Move In/Move Out, Weekly, and Bi-Weekly Cleaning), New Construction Cleaning (Residential, Commercial, and Industrial), and Apartment Turn cleaning for Property Managers. It should list that we carry insurance as well.

Target Market(s)

Residential and Commercial Customers

Industry/Entity Type

Cleaning

Coding

Coded - Design and coding required

Number of Pages Required

5+ page

Requirements
Must have
• A clean professional looking website

```html
<!DOCTYPE html>
<html lang="en">
<head>
<meta charset="utf-8">
<title>BrightNest Cleaning</title>
<link href="https://fonts.googleapis.com/css2?family=Roboto:wght@400;500;700&family=Roboto+Slab:wght@500;700&display=swap" rel="stylesheet">
<style>
:root{
  --blue:#2f86cf;
  --teal:#2fb3a1;
  --ink:#1d1d1d;
  --body:#444;
  --soft:#f3f3f3;
  --white:#fff;
  --gold:#f5b81c;
}
*{box-sizing:border-box;margin:0;padding:0}
html,body{width:1200px;height:4425px;overflow:hidden}
body{font-family:'Roboto',sans-serif;color:var(--body);background:var(--white);position:relative}
.abs{position:absolute}
.slab{font-family:'Roboto Slab',serif}
.btn{position:absolute;background:var(--blue);color:var(--white);font-size:13px;font-weight:500;border-radius:20px;display:flex;align-items:center;justify-content:center}
.heading{font-family:'Roboto Slab',serif;font-weight:700;font-size:36px;text-align:center;position:absolute;left:0;width:1200px}
.heading .t{color:var(--teal)}.heading .b{color:var(--blue)}
.topbar{top:0;left:0;width:1200px;height:43px;background:var(--blue);color:var(--white);font-size:11px;font-weight:500}
.topbar .item{position:absolute;top:12px;display:flex;align-items:center;gap:10px}
.ring{width:22px;height:22px;border-radius:50%;border:1.5px solid var(--white);display:inline-block}
.nav{top:43px;left:0;width:1200px;height:86px;background:var(--white);border-bottom:1px solid #e5e5e5}
.brand{display:flex;align-items:center;gap:10px;font-family:'Roboto',sans-serif;font-weight:700;color:var(--teal)}
.brand .sq{background:var(--blue);border-radius:4px}
.menu{position:absolute;top:37px;font-size:13px;color:var(--ink)}
.hero{top:129px;left:0;width:1200px;height:523px;background:linear-gradient(90deg,#9a9a9a 0%,#c8c8c8 45%,#8a8d92 70%,#3c4a5c 100%)}
.hero h1{position:absolute;left:141px;top:150px;width:480px;font-family:'Roboto Slab',serif;font-weight:700;font-size:41px;line-height:56px;color:var(--white)}
.step{position:absolute;width:300px;text-align:center}
.step .circ{width:100px;height:100px;border-radius:50%;background:var(--blue);margin:0 auto;display:flex;align-items:center;justify-content:center}
.step h3{font-family:'Roboto Slab',serif;font-weight:500;font-size:22px;color:var(--ink);margin-top:38px}
.step p{font-size:12.5px;line-height:22px;width:220px;margin:12px auto 0}
.about{top:1188px;left:0;width:1200px;height:531px;background:var(--soft)}
.about p{font-size:12.5px;line-height:22.5px}
.card{position:absolute;background:var(--white);border-radius:8px;box-shadow:0 2px 12px rgba(0,0,0,.1)}
.svc h3{position:absolute;left:22px;top:100px;font-size:21px;font-weight:500;color:var(--ink)}
.svc p{position:absolute;left:22px;top:137px;width:380px;font-size:12.5px;line-height:22.5px}
.svc svg{position:absolute;left:22px;top:24px}
.reviews{top:2538px;left:0;width:1200px;height:480px;background:var(--soft)}
.rev p{position:absolute;left:19px;top:28px;width:250px;font-size:12.5px;line-height:22.5px}
.rev .av{position:absolute;left:19px;top:138px;width:56px;height:56px;border-radius:50%;background:linear-gradient(135deg,#d9c3b0,#7a5a48)}
.rev .nm{position:absolute;left:92px;top:148px;font-size:13px;font-weight:700;color:var(--ink)}
.rev .st{position:absolute;left:92px;top:166px;color:var(--gold);font-size:12px;letter-spacing:1px}
.rev .q{position:absolute;right:22px;top:128px;font-family:'Roboto Slab',serif;font-size:90px;line-height:90px;color:#cfe0f2}
.arrow{position:absolute;width:28px;height:28px;border-radius:50%;border:1.5px solid #333;display:flex;align-items:center;justify-content:center}
.partner{position:absolute;display:flex;align-items:center;gap:8px;font-size:21px;font-weight:500;color:var(--ink)}
.partner i{display:inline-block;width:22px;height:22px;border-radius:50%}
.cta{top:3357px;left:0;width:1200px;height:369px}
.footer{top:4049px;left:0;width:1200px;height:341px;background:var(--soft)}
.fcol h4{font-size:17px;font-weight:500;color:var(--teal)}
.fcol li{list-style:none;font-size:13px;color:var(--ink)}
.fline{display:flex;gap:12px;font-size:13px;color:var(--ink);line-height:22px}
.dot{width:34px;height:34px;border-radius:50%;background:var(--blue);flex:none;display:flex;align-items:center;justify-content:center}
.copy{top:4390px;left:0;width:1200px;height:35px;background:var(--blue);color:var(--white);font-size:12px;font-weight:500;display:flex;align-items:center;justify-content:center}
</style>
</head>
<body>

<header class="abs topbar">
  <div class="item" style="left:141px"><span class="ring"></span>hello@brightnestclean.com</div>
  <div class="item" style="left:552px"><span class="ring"></span>(555) 014-2290</div>
  <div class="item" style="left:890px">Follow Us On <span class="ring"></span><span class="ring"></span><span class="ring"></span></div>
</header>

<nav class="abs nav">
  <div class="brand abs" style="left:141px;top:22px;font-size:22px"><span class="sq" style="width:30px;height:30px"></span>BRIGHTNEST</div>
  <span class="menu" style="left:570px;color:var(--blue);font-weight:500">Home</span>
  <span class="menu" style="left:645px">About Us</span>
  <span class="menu" style="left:740px">Services ⌄</span>
  <span class="menu" style="left:842px">Insurance</span>
  <span class="btn" style="left:932px;top:32px;width:126px;height:32px">Contact Us</span>
</nav>

<section class="abs hero" role="img" aria-label="Cleaner in gloves holding a basket of cleaning supplies in a bright living room">
  <h1>Quality Driven And Reliable To Take Care Of All Your Cleaning</h1>
  <span class="btn" style="left:141px;top:345px;width:127px;height:33px">Contact Us</span>
</section>

<h2 class="heading" style="top:716px"><span class="t">How It </span><span class="b">Works</span></h2>
<div class="step" style="left:101px;top:807px">
  <div class="circ"><svg width="48" height="48" viewBox="0 0 48 48" fill="none" stroke="#fff" stroke-width="2.5"><rect x="12" y="4" width="24" height="40" rx="4"/><path d="M18 22l5 5 9-10"/></svg></div>
  <h3>Book a Clean Online</h3>
  <p>Lorem Ipsum has been the industry's standard dummy text ever since the 1500s, when an unknown</p>
</div>
<div class="step" style="left:441px;top:807px">
  <div class="circ"><svg width="48" height="48" viewBox="0 0 48 48" fill="none" stroke="#fff" stroke-width="2.5"><path d="M10 44V20h14v24zM17 20V8h-5M30 44l4-30h6l4 30z"/></svg></div>
  <h3>We do The Clean Work</h3>
  <p>Lorem Ipsum has been the industry's standard dummy text ever since the 1500s, when an unknown</p>
</div>
<div class="step" style="left:781px;top:807px">
  <div class="circ"><svg width="48" height="48" viewBox="0 0 48 48" fill="none" stroke="#fff" stroke-width="2.5"><circle cx="30" cy="14" r="6"/><path d="M30 2v4M42 14h-4M22 14h-4M6 40l14-10h22M10 44h32"/></svg></div>
  <h3>You Sit Back And Relax</h3>
  <p>Lorem Ipsum has been the industry's standard dummy text ever since the 1500s, when an unknown</p>
</div>
<span class="btn" style="left:527px;top:1068px;width:146px;height:34px">Book A Cleaning</span>

<section class="abs about">
  <div class="abs" role="img" aria-label="Bright modern living room interior" style="left:244px;top:84px;width:341px;height:282px;border-radius:10px;background:linear-gradient(160deg,#e9e4dc,#b89a74 70%,#8c6f52)"></div>
  <div class="abs" role="img" aria-label="Cleaner vacuuming an office hallway" style="left:141px;top:277px;width:196px;height:168px;border-radius:8px;border:3px solid #fff;background:linear-gradient(160deg,#cfd6de,#5d6f84 60%,#c9a62a)"></div>
  <div class="abs" style="left:380px;top:392px;font-size:24px;font-weight:500;color:#a9dcd5;letter-spacing:2px">BRIGHTNEST</div>
  <h2 class="abs slab" style="left:622px;top:90px;font-size:34px;font-weight:700;color:var(--teal)">About Us</h2>
  <div class="abs slab" style="left:622px;top:146px;font-size:15px;font-weight:500;color:var(--ink)">Lorem Ipsum is simply dummy and typesetting industry.</div>
  <p class="abs" style="left:622px;top:180px;width:440px">Lorem Ipsum is simply dummy text of the printing and typesetting industry. Lorem Ipsum has been the industry's standard dummy text ever since the to same 1500s, when an unknown printer took a galley of type and scrambled it to type specimen book. It has survived not only five centuries, but also the leap into electronic typesetting, remaining essentially unchanged.</p>
  <p class="abs" style="left:622px;top:302px;width:440px">Lorem Ipsum is simply dummy text of the printing and typesetting industry. to Lorem Ipsum has been the industry's standard dummy text ever since the 1500s, when an unknown printer took a galley make a type of specimen book lorem ipsum is simply dummy text.</p>
  <span class="btn" style="left:622px;top:412px;width:123px;height:34px">Read More</span>
</section>

<h2 class="heading" style="top:1806px"><span class="t">Services </span><span class="b">We Offer</span></h2>
<div class="card svc" style="left:141px;top:1894px;width:444px;height:230px">
  <svg width="64" height="60" viewBox="0 0 64 60" fill="none" stroke="var(--blue)" stroke-width="2"><path d="M4 28L32 6l28 22M10 24v32h44V24M26 56V40h12v16M16 32h8v8h-8zM40 32h8v8h-8z"/></svg>
  <h3>Residential Cleaning</h3>
  <p>Lorem Ipsum has been the industry's standard dummy text ever since the 1500s, when an printer took read specimen book.</p>
</div>
<div class="card svc" style="left:613px;top:1894px;width:445px;height:230px">
  <svg width="64" height="60" viewBox="0 0 64 60" fill="none" stroke="var(--blue)" stroke-width="2"><path d="M6 56h54M12 56V10h30v46M42 20h14v36M18 18h6M30 18h6M18 28h6M30 28h6M18 38h6M30 38h6"/></svg>
  <h3>Commercial Cleaning</h3>
  <p>Lorem Ipsum has been the industry's standard dummy text ever since the 1500s, when an printer took read specimen book.</p>
</div>
<div class="card svc" style="left:141px;top:2151px;width:444px;height:230px">
  <svg width="64" height="60" viewBox="0 0 64 60" fill="none" stroke="var(--blue)" stroke-width="2"><circle cx="38" cy="36" r="12"/><path d="M30 44l16-16M10 10l4 4M14 10l-4 4M6 40l4 4M10 40l-4 4M22 6v10M18 22v20"/></svg>
  <h3>Antiviral Disinfection</h3>
  <p>Lorem Ipsum has been the industry's standard dummy text ever since the 1500s, when an printer took read specimen book.</p>
</div>
<div class="card svc" style="left:613px;top:2151px;width:445px;height:230px">
  <svg width="64" height="60" viewBox="0 0 64 60" fill="none" stroke="var(--blue)" stroke-width="2"><path d="M6 44h44l8-20H14zM14 24l8-14h30M10 52h44"/></svg>
  <h3>Construction Cleaning</h3>
  <p>Lorem Ipsum has been the industry's standard dummy text ever since the 1500s, when an printer took read specimen book.</p>
</div>
<span class="btn" style="left:527px;top:2418px;width:146px;height:34px">Book A Cleaning</span>

<section class="abs reviews">
  <h2 class="heading" style="top:85px"><span class="t">Customer </span><span class="b">Reviews</span></h2>
  <span class="arrow" style="left:96px;top:269px">←</span>
  <span class="arrow" style="left:1071px;top:269px">→</span>
  <div class="card rev" style="left:141px;top:171px;width:288px;height:224px">
    <p>Lorem Ipsum has been the industry's to standard dummy text ever since the 1500s, when an printer took read the specimen book.</p>
    <span class="av" role="img" aria-label="Customer portrait"></span><span class="nm">Dana R</span><span class="st">★★★★★</span><span class="q">”</span>
  </div>
  <div class="card rev" style="left:455px;top:171px;width:288px;height:224px">
    <p>Lorem Ipsum has been the industry's to standard dummy text ever since the 1500s, when an printer took read the specimen book.</p>
    <span class="av" role="img" aria-label="Customer portrait"></span><span class="nm">Leo Marsh</span><span class="st">★★★★★</span><span class="q">”</span>
  </div>
  <div class="card rev" style="left:769px;top:171px;width:289px;height:224px">
    <p>Lorem Ipsum has been the industry's to standard dummy text ever since the 1500s, when an printer took read the specimen book.</p>
    <span class="av" role="img" aria-label="Customer portrait"></span><span class="nm">Priya K</span><span class="st">★★★★★</span><span class="q">”</span>
  </div>
</section>

<h2 class="abs slab" style="left:141px;top:3110px;font-size:35px;line-height:47px;font-weight:700"><span style="color:var(--teal)">Insurance Companies</span><br><span style="color:var(--blue)">We Support</span></h2>
<p class="abs" style="left:141px;top:3210px;width:380px;font-size:12.5px;line-height:22.5px">Lorem Ipsum has been the industry's standard dummy text ever since the 1500s, when an printer took read specimen book.</p>
<div class="partner" style="left:587px;top:3119px"><i style="background:#333"></i>Northline</div>
<div class="partner" style="left:758px;top:3119px"><i style="background:#e8542a"></i>Harborway</div>
<div class="partner" style="left:935px;top:3119px"><i style="background:#e0417a"></i>Keystone</div>
<div class="partner" style="left:587px;top:3222px"><i style="background:#333"></i>Brightpath</div>
<div class="partner" style="left:758px;top:3222px"><i style="background:#f1a51c"></i>Summit</div>
<div class="partner" style="left:935px;top:3222px"><i style="background:#2e8a63"></i>Meadowell</div>

<section class="abs cta">
  <div class="abs" role="img" aria-label="Woman in yellow gloves wiping a wooden table in a living room" style="left:0;top:0;width:600px;height:369px;background:linear-gradient(135deg,#5c5e60,#c9c3b8 50%,#b9884f)"></div>
  <svg class="abs" style="left:0;top:0" width="1200" height="369"><polygon points="460,0 1200,0 1200,369 450,369 558,184" fill="var(--blue)"/></svg>
  <h2 class="abs slab" style="left:603px;top:100px;font-size:34px;line-height:46px;font-weight:700;color:var(--white)">Expert Cleaning And<br>Maintenance Services<br>For Your Home Or Business</h2>
  <span class="btn" style="left:603px;top:249px;width:144px;height:32px;background:var(--white);color:var(--blue)">Book A Cleaning</span>
</section>

<h2 class="heading" style="top:3810px"><span class="t">Your Trust And Security </span><span class="b">Is Our Priority</span></h2>
<p class="abs" style="left:0;top:3868px;width:1200px;text-align:center;font-size:12.5px;line-height:21px">Lorem Ipsum has been the industry's to standard dummy text ever since<br>the 1500s, when an printer took read the specimen book.</p>
<span class="btn" style="left:527px;top:3928px;width:146px;height:34px">Book A Cleaning</span>

<footer class="abs footer">
  <div class="brand abs" style="left:141px;top:100px;font-size:32px"><span class="sq" style="width:40px;height:40px"></span>BRIGHTNEST</div>
  <div class="fcol abs" style="left:450px;top:78px">
    <h4>Quick Links</h4>
    <ul style="margin-top:16px;line-height:33px"><li>Home</li><li>About Us</li><li>Services</li><li>Insurance</li><li>Contact Us</li></ul>
  </div>
  <div class="fcol abs" style="left:632px;top:78px">
    <h4>Contact us</h4>
    <div class="fline" style="margin-top:14px"><span class="dot"><svg width="14" height="16" viewBox="0 0 14 16" fill="none" stroke="#fff" stroke-width="1.6"><path d="M7 15s5-5 5-9A5 5 0 0 0 2 6c0 4 5 9 5 9z"/><circle cx="7" cy="6" r="1.6"/></svg></span><span>48 Maple Row, Suite 2,<br>Fairview, ST 10024</span></div>
    <div class="fline" style="margin-top:12px"><span class="dot"><svg width="14" height="14" viewBox="0 0 14 14" fill="none" stroke="#fff" stroke-width="1.6"><path d="M3 1l2 3-1.5 1.5a8 8 0 0 0 5 5L10 9l3 2-1 2C6 13 1 8 1 2z"/></svg></span><span>Phone<br>(555) 014-2290</span></div>
    <div class="fline" style="margin-top:12px"><span class="dot"><svg width="16" height="12" viewBox="0 0 16 12" fill="none" stroke="#fff" stroke-width="1.6"><rect x="1" y="1" width="14" height="10"/><path d="M1 1l7 6 7-6"/></svg></span><span>Email<br>hello@brightnestclean.com</span></div>
  </div>
  <div class="fcol abs" style="left:941px;top:78px">
    <h4>Follow Us On</h4>
    <div class="fline" style="margin-top:16px;align-items:center"><span class="dot"></span>Social One</div>
    <div class="fline" style="margin-top:16px;align-items:center"><span class="dot"></span>Social Two</div>
    <div class="fline" style="margin-top:16px;align-items:center"><span class="dot"></span>Social Three</div>
  </div>
</footer>
<div class="abs copy">© 2024 BRIGHTNEST CLEANING. All Rights Reserved</div>

</body>
</html>
```